Design a Online payment portal

We have a mobile money transfer company, We now want to provide an online platform for companies to fill in transfer details to, say, 1,000 employees then the transfer list is electronically available to us through the website.

I need a website that basically works like a bank account and people (client) can log on to the website and create accounts.

We the administrators then activate the account once details are provided by them.

Then client then deposits an amount (outside the payment platform) and the administrator can then "load" this as virtual money or as a balance on the client's account.

The platform provides tools for workflows, approvals and rejections, comments, attachments,

After final approval by the client's top boss or whoever is designated as the signatory/approver, we at the back end process the transfer of funds.

but transaction initiators working mostly on excel files may not need so much of the mobile.

The platform should generate notifications every time a transaction happens. it should generate reports as well.

we would also need to charge for each transaction on the platform.

Industry/Entity Type

It Company

```html
<!DOCTYPE html>
<html lang="en">
<head>
<meta charset="utf-8">
<title>Payvane – Pay online, safely and easily</title>
<link href="https://fonts.googleapis.com/css2?family=Arimo:wght@400;700&display=swap" rel="stylesheet">
<style>
  :root {
    --white: #ffffff;
    --ink: #333333;
    --muted: #666666;
    --nav-bg: #eeeeee;
    --card-bg: #f2f2f2;
    --card-line: #dcdcdc;
    --green: #5cb85c;
    --green-dark: #1e9a5c;
    --blue-btn: #428bca;
    --teal: #1aa88f;
    --teal-dark: #1e7e6e;
    --gear: #1a9ee0;
    --accent-red: #e8431e;
    --footer-bg: #ebebeb;
    --social: #3b86c6;
  }
  * { box-sizing: border-box; margin: 0; padding: 0; }
  html, body { width: 1200px; height: 580px; overflow: hidden; }
  body {
    position: relative;
    font-family: "Arimo", Arial, sans-serif;
    color: var(--ink);
    background: var(--footer-bg);
  }
  .topbar {
    position: absolute; left: 0; top: 0; width: 1200px; height: 53px;
    background: var(--white);
    box-shadow: 0 1px 4px rgba(0,0,0,.12);
    z-index: 2;
  }
  .site-title {
    position: absolute; left: 103px; top: 10px;
    font-size: 21px; font-weight: 400; color: var(--muted);
  }
  .btn {
    position: absolute; top: 14px; height: 30px;
    border-radius: 3px; color: var(--white);
    font-size: 13px; line-height: 30px; text-align: center;
  }
  .btn-signup { left: 980px; width: 64px; background: var(--blue-btn); border: 1px solid #357ebd; }
  .btn-login { left: 1049px; width: 53px; background: var(--green); border: 1px solid #4cae4c; }
  .mainnav {
    position: absolute; left: 0; top: 53px; width: 1200px; height: 42px;
    background: var(--nav-bg);
  }
  .mainnav ul { list-style: none; display: flex; gap: 18px; position: absolute; left: 105px; top: 17px; }
  .mainnav li { font-size: 14px; font-variant: small-caps; color: #444; }
  .hero {
    position: absolute; left: 0; top: 95px; width: 1200px; height: 311px;
    background: linear-gradient(90deg, #b4aeaa 0%, #cfcac6 18%, #9c9591 35%, #e8e6e3 50%, #bdb8b3 62%, #8c8884 78%, #4a4745 92%, #2d2c2b 100%);
  }
  .feature {
    position: absolute; top: 148px; width: 320px; height: 223px;
    background: var(--card-bg); border: 1px solid var(--card-line);
    text-align: center;
  }
  .feature-1 { left: 93px; }
  .feature-2 { left: 440px; }
  .feature-3 { left: 787px; }
  .feature-badge {
    position: absolute; left: 138px; top: -23px; width: 44px; height: 44px;
    border-radius: 50%; background: var(--green);
    display: flex; align-items: center; justify-content: center;
  }
  .feature h2 { margin-top: 40px; font-size: 18px; font-weight: 400; color: #3a3a3a; }
  .feature p { margin: 29px 16px 0; font-size: 12.5px; line-height: 14px; color: var(--teal); }
  .feature-icon { margin-top: 12px; }
  .card-name { margin-top: 20px; font-size: 22px; font-weight: 700; color: #333; }
  .quote-badge {
    position: absolute; left: 1049px; top: 376px; width: 42px; height: 42px;
    border-radius: 50%; background: var(--green-dark);
    box-shadow: 0 3px 6px rgba(0,0,0,.35);
    display: flex; align-items: center; justify-content: center;
  }
  .footer-col { position: absolute; }
  .footer-brand { left: 73px; top: 506px; width: 340px; }
  .footer-brand h3 { font-size: 14px; font-weight: 400; color: var(--accent-red); }
  .footer-brand p { margin-top: 4px; font-size: 10px; line-height: 15px; color: var(--muted); }
  .footer-about { left: 433px; top: 466px; width: 340px; }
  .footer-col h4 { font-size: 14.5px; font-weight: 400; color: var(--teal-dark); }
  .footer-about p { margin-top: 10px; font-size: 12px; line-height: 18px; color: #777; }
  .footer-social { left: 793px; top: 466px; }
  .social-links { display: flex; gap: 9px; margin-top: 14px; margin-left: 4px; }
  .social-links span { width: 21px; height: 21px; border-radius: 3px; background: var(--social); display: block; }
</style>
</head>
<body>
  <header class="topbar">
    <div class="site-title">Pay online, Safely and easily</div>
    <a class="btn btn-signup">SignUp</a>
    <a class="btn btn-login">Login</a>
  </header>

  <nav class="mainnav">
    <ul>
      <li>Home</li><li>Personal</li><li>Business</li><li>About</li><li>Register</li><li>Login</li>
    </ul>
  </nav>

  <section class="hero" role="img" aria-label="Blurred office interior background photo"></section>

  <article class="feature feature-1">
    <div class="feature-badge">
      <svg width="20" height="20" viewBox="0 0 20 20" fill="none" stroke="#fff" stroke-width="2" stroke-linecap="round">
        <circle cx="10" cy="4" r="2"/><line x1="10" y1="6" x2="10" y2="17"/><line x1="6" y1="9" x2="14" y2="9"/>
        <path d="M3 12 Q4 17 10 17 Q16 17 17 12"/>
      </svg>
    </div>
    <h2>Exclusive Payvane Offers</h2>
    <p>Visit our brand new Promotions Centre for our latest unmissable offers</p>
    <svg class="feature-icon" width="60" height="52" viewBox="0 0 60 52">
      <path d="M2 4 H12 L20 36 H52" fill="none" stroke="#2f2f2f" stroke-width="5" stroke-linejoin="round"/>
      <path d="M14 10 H58 V32 H20 Z" fill="#2f2f2f"/>
      <rect x="33" y="13" width="5" height="16" fill="#fff"/><rect x="27" y="18.5" width="17" height="5" fill="#fff"/>
      <circle cx="24" cy="46" r="4.5" fill="#2f2f2f"/><circle cx="48" cy="46" r="4.5" fill="#2f2f2f"/>
    </svg>
  </article>

  <article class="feature feature-2">
    <div class="feature-badge">
      <svg width="22" height="18" viewBox="0 0 22 18" fill="#fff">
        <path d="M2 2 V16 H21" fill="none" stroke="#fff" stroke-width="2"/>
        <path d="M4 14 L4 9 L8 5 L12 9 L15 6 L19 10 L19 14 Z"/>
      </svg>
    </div>
    <h2>Pay online, safely</h2>
    <p>Whenever you pay and shop online, pay with Payvane</p>
    <svg class="feature-icon" width="60" height="60" viewBox="0 0 60 60">
      <g fill="var(--gear)" transform="translate(30 30)">
        <rect x="-6" y="-29" width="12" height="14" rx="2"/>
        <rect x="-6" y="-29" width="12" height="14" rx="2" transform="rotate(45)"/>
        <rect x="-6" y="-29" width="12" height="14" rx="2" transform="rotate(90)"/>
        <rect x="-6" y="-29" width="12" height="14" rx="2" transform="rotate(135)"/>
        <rect x="-6" y="-29" width="12" height="14" rx="2" transform="rotate(180)"/>
        <rect x="-6" y="-29" width="12" height="14" rx="2" transform="rotate(225)"/>
        <rect x="-6" y="-29" width="12" height="14" rx="2" transform="rotate(270)"/>
        <rect x="-6" y="-29" width="12" height="14" rx="2" transform="rotate(315)"/>
        <circle r="21"/>
      </g>
      <circle cx="30" cy="30" r="9" fill="#fff"/>
    </svg>
  </article>

  <article class="feature feature-3">
    <div class="feature-badge">
      <svg width="22" height="16" viewBox="0 0 22 16" fill="#fff">
        <rect x="1" y="1" width="2.5" height="14"/><circle cx="7" cy="6" r="2.5"/>
        <path d="M10 4 H18 Q21 4 21 8 V11 H3 V9 H10 Z"/><rect x="18.5" y="11" width="2.5" height="4"/>
      </svg>
    </div>
    <h2>Get paid globally</h2>
    <p>However your customers pay, checkout with Payvane.</p>
    <div class="card-name">Cardex</div>
  </article>

  <div class="quote-badge">
    <svg width="18" height="14" viewBox="0 0 18 14" fill="#fff">
      <path d="M1 1 H7 V7 L4 13 H1 L3 7 H1 Z"/><path d="M10 1 H16 V7 L13 13 H10 L12 7 H10 Z"/>
    </svg>
  </div>

  <footer>
    <div class="footer-col footer-brand">
      <h3>Pay online, safely and easily.</h3>
      <p>With Payvane your financial details are always safe when you shop and pay online.</p>
    </div>
    <div class="footer-col footer-about">
      <h4>About Us</h4>
      <p>An e-commerce payment system facilitates the acceptance of electronic payment for online transactions. Also known as a sample of Electronic Data Interchange (EDI)</p>
    </div>
    <div class="footer-col footer-social">
      <h4>Social</h4>
      <div class="social-links"><span></span><span></span><span></span></div>
    </div>
  </footer>
</body>
</html>
```